Meridian Clearsound Wellness LLC Card Design

Need business card with a logo for a hearing aid sales and audiology business. We have two Hearing Instrument Specialists and one Audiologist on staff. Over 25 years in business. Locally owned and operated. Financing available. Most insurances accepted.

Meridian Clearsound Wellness LLC
48730 W Larkfield, Suite 9
Spokane, WA 99371
509-617-2084
www.meridianclearsound-example.com

Manager
Tobias Wrenfield HIS COHC
License #81957260

Target Market(s)

50yr old + people with a hearing loss.

Industry/Entity Type

Business

Contact Information for Business Card

48730 W Larkfield, Suite 9
Spokane, WA 99371
509-617-2084
www.meridianclearsound-example.com

Manager
Tobias Wrenfield HIS COHC
RTEQ #81957260

Font styles to use
Serif
Sans Serif

Requirements
Must have
• Business name, Tobias's name and title(s) and contact information, License #, web address
Nice to have
Should not have

```html
<!DOCTYPE html>
<html lang="en">
<head>
<meta charset="utf-8">
<title>Meridian Clearsound Wellness – Business Card</title>
<link href="https://fonts.googleapis.com/css2?family=Roboto+Condensed:wght@300;400&family=Oswald:wght@400&family=Questrial&display=swap" rel="stylesheet">
<style>
  :root {
    --backdrop: #3b3b3d;
    --card-white: #ffffff;
    --navy: #41567a;
    --logo-blue: #1453a0;
    --name-blue: #34466b;
    --text-grey: #6a6a6a;
    --logo-text: #2b2b2b;
    --frame-grey: #9a9a9a;
  }
  html, body {
    margin: 0; padding: 0;
    width: 1200px; height: 1200px;
    overflow: hidden;
    background: var(--backdrop);
  }
  .canvas { position: relative; width: 1200px; height: 1200px; }
  .card {
    position: absolute;
    left: 265px;
    width: 670px; height: 380px;
    border-radius: 16px;
    overflow: hidden;
  }
  .card-front { top: 190px; background: var(--card-white); }
  .card-back { top: 632px; background: var(--navy); }

  .logo-lockup {
    position: absolute;
    display: flex; align-items: center; gap: 12px;
    width: 250px; height: 82px;
    box-sizing: border-box;
    padding: 0 8px;
    background: var(--card-white);
    border: 1.5px solid var(--frame-grey);
    border-radius: 9px;
  }
  .card-front .logo-lockup { left: 46px; top: 44px; }
  .card-back .logo-lockup { left: 210px; top: 145px; }
  .logo-square {
    flex: none; width: 66px; height: 66px;
    background: var(--logo-blue); border-radius: 6px;
  }
  .logo-name {
    font-family: "Questrial", sans-serif;
    font-size: 17px; line-height: 19px;
    color: var(--logo-text);
  }

  .holder {
    position: absolute; right: 372px; top: 204px;
    text-align: right;
    font-family: "Roboto Condensed", sans-serif; font-weight: 300;
    color: var(--text-grey);
  }
  .holder-name {
    font-family: "Oswald", sans-serif; font-weight: 400;
    font-size: 26px; line-height: 30px;
    color: var(--name-blue); letter-spacing: -0.3px;
    margin: 0 0 2px;
  }
  .holder-role, .holder-license { font-size: 20px; line-height: 26px; margin: 0; }

  .divider {
    position: absolute; left: 339px; top: 178px;
    width: 1.5px; height: 156px; background: var(--name-blue);
  }

  .contact {
    position: absolute; left: 363px; top: 187px;
    font-family: "Roboto Condensed", sans-serif; font-weight: 300;
    font-size: 18px; line-height: 22.5px;
    color: var(--text-grey);
  }
  .contact p { margin: 0; }
  .contact .address { margin-bottom: 20px; }
  .contact-line { display: flex; align-items: center; gap: 8px; }
  .contact-line svg { width: 14px; height: 14px; flex: none; }

  .footer-band { position: absolute; left: 0; bottom: 0; width: 670px; height: 34px; }

  .back-url {
    position: absolute; left: 0; right: 0; top: 330px;
    text-align: center;
    font-family: "Roboto Condensed", sans-serif; font-weight: 400;
    font-size: 19px; color: var(--card-white);
  }
</style>
</head>
<body>
<div class="canvas">

  <section class="card card-front">
    <div class="logo-lockup">
      <span class="logo-square"></span>
      <span class="logo-name">Meridian Clearsound<br>Wellness</span>
    </div>

    <div class="holder">
      <p class="holder-name">TOBIAS WRENFIELD HIS COHC</p>
      <p class="holder-role">Manager</p>
      <p class="holder-license">License #81957260</p>
    </div>

    <div class="divider"></div>

    <div class="contact">
      <p class="address">Meridian Clearsound Wellness LLC<br>48730 W Larkfield, Suite 9<br>Spokane, WA 99371</p>
      <p class="contact-line">
        <svg viewBox="0 0 16 16" aria-hidden="true"><path fill="#555" d="M1 6c0-2 3-3 7-3s7 1 7 3v1h-3.5V5.5h-7V7H1z M4 8h8l1.5 5h-11z"/><circle cx="8" cy="10.5" r="1.6" fill="#fff"/></svg>
        509-617-2084
      </p>
      <p class="contact-line">
        <svg viewBox="0 0 16 16" aria-hidden="true"><g fill="none" stroke="#666" stroke-width="1"><circle cx="8" cy="8" r="6.5"/><ellipse cx="8" cy="8" rx="3" ry="6.5"/><path d="M1.5 8h13M2.5 4.8h11M2.5 11.2h11"/></g></svg>
        www.meridianclearsound-example.com
      </p>
    </div>

    <svg class="footer-band" viewBox="0 0 670 34" aria-hidden="true">
      <polygon points="0,11 352,11 337,34 0,34" fill="var(--navy)"/>
      <polygon points="372,0 670,0 670,34 346,34" fill="var(--navy)"/>
    </svg>
  </section>

  <section class="card card-back">
    <div class="logo-lockup">
      <span class="logo-square"></span>
      <span class="logo-name">Meridian Clearsound<br>Wellness</span>
    </div>
    <p class="back-url">www.meridianclearsound-example.com</p>
  </section>

</div>
</body>
</html>
```